Hi all
We need an artistic, creative and modern business card design for our piano studio. Logo is attached, please let us know if you need other file formats.
The business card should convey high-end, prestigiousness, and be minimalist in feel. It should not look corporate or childish.
Rounded corners or creative shapes only, no regular square corners. Card should be double-sided. Can be portrait or landscape oriented. No preference to size either. Standard or custom size both okay.
We will not be giving out thousands of cards due to the nature of our business. We want to make sure that each business card we hand out, people will appreciate the design and printing quality that took place.
Please note, as the logo is supplied, we need more than just a layout with name and phone number etc inserted. Quite frankly,we can do that ourselves. We are interested in designs that has the different special printing methods in mind during the designing process. We are particularly interested in the effects of:
- Spot UV Varnish
- Foil
- Thermography
- Letterpress
- Die Cut
- Lamination
Colours does not have to be limited to black and white.
Information to be included:
Name (with qualification attached)
Mobile
website "talmer.com.au"
Designs submitted should include description of the printing method. The final format should be ready to be sent to printer with detailed printing method and colour (if applicable) instructions.
Much thanks in advance.
as per request from a designer, eps format file uploaded.

```html
<!DOCTYPE html>
<html lang="en">
<head>
<meta charset="UTF-8">
<title>Talmer Piano Studio — Business Card</title>
<link rel="stylesheet" href="https://fonts.googleapis.com/css2?family=Quicksand:wght@300;700&family=Open+Sans:wght@600&display=swap">
<style>
  :root {
    --backdrop: #e8e5e1;
    --card-black: #0c0c0c;
    --card-white: #ffffff;
    --band-grey: #4d4d4b;
    --ink-white: #ffffff;
    --ink-black: #111111;
    --ink-soft: #2a2a2a;
    --icon-grey: #8a8a8a;
  }
  * { margin: 0; padding: 0; box-sizing: border-box; }
  html, body {
    width: 1200px;
    height: 1073px;
    overflow: hidden;
    background: var(--backdrop);
  }
  .canvas {
    position: relative;
    width: 1200px;
    height: 1073px;
  }
  .card {
    position: absolute;
    top: 180px;
    width: 440px;
    height: 713px;
    border-radius: 28px;
    overflow: hidden;
    box-shadow: 0 10px 30px rgba(0,0,0,0.18);
  }
  .card--front {
    left: 130px;
    background: var(--card-black);
  }
  .card--back {
    left: 630px;
    background: var(--card-white);
  }

  /* Front side */
  .front-name {
    position: absolute;
    top: 118px;
    left: 0;
    width: 100%;
    text-align: center;
    font-family: "Quicksand", sans-serif;
    font-weight: 700;
    font-size: 58px;
    letter-spacing: 4px;
    color: var(--ink-white);
  }
  .front-tagline {
    position: absolute;
    top: 238px;
    left: 0;
    width: 100%;
    text-align: center;
    font-family: "Quicksand", sans-serif;
    font-weight: 300;
    font-size: 27px;
    letter-spacing: 7px;
    color: var(--ink-white);
  }
  .front-band {
    position: absolute;
    top: 485px;
    left: 128px;
    right: 0;
    height: 66px;
    background: var(--band-grey);
    border-radius: 33px 0 0 33px;
    display: flex;
    align-items: center;
    padding-left: 20px;
    gap: 22px;
  }
  .front-band svg { flex: none; }
  .front-band-name {
    font-family: "Quicksand", sans-serif;
    font-weight: 700;
    font-size: 42px;
    letter-spacing: 3px;
    color: var(--ink-white);
  }

  /* Back side */
  .back-name {
    position: absolute;
    top: 110px;
    left: 0;
    width: 100%;
    text-align: center;
    font-family: "Quicksand", sans-serif;
    font-weight: 700;
    font-size: 56px;
    letter-spacing: 4px;
    color: var(--ink-black);
  }
  .back-tagline {
    position: absolute;
    top: 196px;
    left: 0;
    width: 100%;
    text-align: center;
    font-family: "Quicksand", sans-serif;
    font-weight: 300;
    font-size: 26px;
    letter-spacing: 7px;
    color: var(--ink-soft);
  }
  .back-tab {
    position: absolute;
    top: 485px;
    left: 0;
    width: 96px;
    height: 66px;
    background: var(--band-grey);
    border-radius: 0 33px 33px 0;
  }
  .contact {
    position: absolute;
    left: 118px;
    bottom: 70px;
    list-style: none;
    font-family: "Open Sans", sans-serif;
    font-weight: 600;
    font-size: 17px;
    color: var(--ink-black);
  }
  .contact li {
    display: flex;
    align-items: center;
    gap: 18px;
    height: 34px;
  }
  .contact .icon { width: 18px; flex: none; }
  .contact .web { padding-left: 36px; }
</style>
</head>
<body>
<main class="canvas">

  <section class="card card--front" aria-label="Front of card">
    <div class="front-name">TALMER</div>
    <div class="front-tagline">PIANO STUDIO</div>
    <div class="front-band">
      <svg width="40" height="40" viewBox="0 0 40 40" aria-hidden="true">
        <circle cx="20" cy="20" r="17" fill="none" stroke="#ffffff" stroke-width="3"/>
        <path d="M11 20h16M21 13l7 7-7 7" fill="none" stroke="#ffffff" stroke-width="3.2" stroke-linecap="round" stroke-linejoin="round"/>
      </svg>
      <span class="front-band-name">TALMER</span>
    </div>
  </section>

  <section class="card card--back" aria-label="Back of card">
    <div class="back-name">TALMER</div>
    <div class="back-tagline">PIANO STUDIO</div>
    <div class="back-tab"></div>
    <ul class="contact">
      <li>
        <svg class="icon" viewBox="0 0 18 18" aria-hidden="true">
          <path d="M4 2c1 0 2 2.5 2 3.2 0 .8-1.2 1.2-1 2 .5 1.8 2 3.4 3.8 4 .8.2 1.2-1 2-1 .7 0 3.2 1 3.2 2s-1.5 3-3 3C7 15 3 11 2.5 6 2.3 4 3 2 4 2z" fill="var(--icon-grey)"/>
        </svg>
        <span>+00 000 000 000</span>
      </li>
      <li>
        <svg class="icon" viewBox="0 0 18 18" aria-hidden="true">
          <rect x="1.5" y="4" width="15" height="10" fill="none" stroke="var(--icon-grey)" stroke-width="1.3"/>
          <path d="M1.5 4l7.5 6 7.5-6M1.5 14l5.5-5M16.5 14l-5.5-5" fill="none" stroke="var(--icon-grey)" stroke-width="1.3"/>
        </svg>
        <span>your e-mail@email.com</span>
      </li>
      <li class="web"><span>www.talmer.com.au</span></li>
    </ul>
  </section>

</main>
</body>
</html>
```